Email PDF Guide for Quillbrook

We are an online professional services website which helps start ups and small businesses gain access to the R&D tax incentive.

We want to educate businesses across multiple industries to understand what they need to do to access this tax incentive, with information relevant to their industry. We need a designer to pull together and design images and relevant visuals for a downloadable guide. Please note - we will provide all the content for this, your job is to pull this into a stylised guide, which is inviting to our audience and compliment the words with imagery.

We are looking to produce 12 guides in total but will start with one to confirm design and style. Then follow up with remaining 11 industries.

First industry: Technology and Software

To get a sense for what we do our site is: https://www.quillbrook.example/

Very interested to hear what the community comes up with to create something visually engaging and relevant to our site and message.

Target Market(s)

Start up founders and entrepreneurs in technology industry. Average age 35.

Industry/Entity Type

Information Technology

Font styles to use
Other font styles liked:
• Proxima Nova

Requirements
Must have
• - Guide needs to be minimum of 8 pages, content currently totals 5 word pages.
• - The format needs to be editable on standard Google or Microsoft products then formatted into PDF, so we can make text changes at later dates (can discuss this criteria if difficult)
• - Font is Proxima Nova
• - Colours and gradients can be found here: http://tadvelin.samplehost.example/
• - Colour selection should be:
• * Main palette = #ff7c14 , #ffa800 , #fc4e78
• * Gray palette = #cccccc , #c1d1d9 , #f5f7f9 , #080808 , #2d3338 , #666666 , #6f7c82 , #999999
Nice to have
• Play with the title for best design format.
• Happy with one of the following options:
• - R&D in the Technology Industry
• - What you need to know about R&D in Technologu

```html
<!DOCTYPE html>
<html lang="en">
<head>
<meta charset="utf-8">
<title>Quillbrook R&amp;D – Technology Guide</title>
<link rel="stylesheet" href="https://fonts.googleapis.com/css2?family=Montserrat:wght@300;400;500;600;700&display=swap">
<style>
  :root {
    --stage: #5e5e5e;
    --paper: #ffffff;
    --brand-red: #a82125;
    --brand-orange: #e07b2d;
    --brand-amber: #f3b82b;
    --brand-pink: #cf5e8f;
    --brand-coral: #df7a58;
    --ink: #333333;
    --body: #555555;
    --rule: #777777;
    --footer-pink: #d4535a;
  }
  * { box-sizing: border-box; margin: 0; padding: 0; }
  html, body { width: 1200px; height: 1000px; overflow: hidden; }
  body {
    background: var(--stage);
    font-family: "Montserrat", sans-serif;
    position: relative;
  }
  .page {
    position: absolute;
    top: 125px;
    width: 530px;
    height: 748px;
    background: var(--paper);
    overflow: hidden;
  }
  .page--cover { left: 60px; }
  .page--inner { left: 611px; width: 529px; }

  /* cover header */
  .cover-curve { position: absolute; left: 0; top: 0; }
  .cover-blocks {
    position: absolute; left: 403px; top: 0; width: 127px; height: 120px;
    background: linear-gradient(180deg, var(--brand-coral) 0%, var(--brand-orange) 55%, var(--brand-amber) 100%);
  }
  .wordmark {
    display: flex; align-items: center; gap: 8px;
    font-weight: 700; color: var(--ink); white-space: nowrap;
  }
  .wordmark__square { width: 12px; height: 12px; background: var(--brand-red); flex: none; }
  .cover-wordmark { position: absolute; left: 30px; top: 64px; font-size: 20px; }
  .product-name {
    position: absolute; left: 167px; top: 58px;
    font-size: 26px; font-weight: 400; color: var(--ink); white-space: nowrap;
  }
  .title-band {
    position: absolute; left: 0; top: 120px; width: 100%; height: 80px;
    background: var(--brand-red);
    border-bottom: 6px solid var(--brand-orange);
    padding: 12px 0 0 47px;
  }
  .title-band h1 {
    color: #fff; font-size: 23px; font-weight: 700; line-height: 1.3;
  }

  .section { position: absolute; left: 22px; right: 30px; }
  .section__heading {
    display: flex; align-items: center; gap: 20px;
    color: var(--brand-red); font-size: 20px; font-weight: 700;
    margin-bottom: 12px; white-space: nowrap;
  }
  .section__marker { width: 22px; height: 22px; background: var(--brand-orange); flex: none; border-bottom: 4px solid var(--brand-red); }
  .section__body { padding-left: 44px; }
  .section__body p {
    font-size: 10.3px; font-weight: 400; line-height: 1.27; color: var(--body);
  }
  .section__body p + p { margin-top: 12px; }
  .section__body .lead { font-weight: 500; color: var(--ink); }

  .divider { position: absolute; height: 1px; background: var(--rule); }

  .footer-stripes {
    position: absolute; left: 0; bottom: 0; width: 100%; height: 23px;
    background: linear-gradient(180deg,
      var(--footer-pink) 0 11px, var(--brand-orange) 11px 13px,
      var(--brand-red) 13px 16px, var(--brand-amber) 16px 17px,
      var(--footer-pink) 17px 23px);
  }

  /* inner page */
  .inner-band {
    position: absolute; left: 0; top: 0; width: 100%; height: 48px;
    background: var(--brand-red); border-bottom: 2px solid var(--brand-orange);
  }
  .section--intro-inner { right: 48px; }
  .industry-list { list-style: none; margin: 18px 0 0 14px; }
  .industry-list li {
    display: flex; align-items: center; gap: 9px;
    font-size: 10.3px; color: var(--body); line-height: 16px;
  }
  .industry-list li::before {
    content: ""; width: 8px; height: 8px; background: var(--brand-orange);
    border-bottom: 2px solid var(--brand-red);
  }
  .inner-lockup {
    position: absolute; left: 318px; top: 294px;
    display: flex; align-items: center; gap: 12px; white-space: nowrap;
  }
  .inner-lockup .wordmark { font-size: 12px; }
  .inner-lockup .wordmark__square { width: 8px; height: 8px; }
  .inner-lockup .product { font-size: 12px; color: var(--ink); }
</style>
</head>
<body>

<article class="page page--cover">
  <svg class="cover-curve" width="530" height="125" viewBox="0 0 530 125" aria-hidden="true">
    <path d="M230 120 C 330 100, 410 60, 420 0 L530 0 L530 120 Z" fill="var(--brand-pink)"/>
  </svg>
  <div class="cover-blocks" role="img" aria-label="Decorative warm colour blocks"></div>

  <div class="wordmark cover-wordmark"><span class="wordmark__square"></span>Veltmark</div>
  <div class="product-name">Quillbrook R&amp;D</div>

  <header class="title-band">
    <h1>What you need to know about R&amp;D<br>in the technology industry</h1>
  </header>

  <section class="section" style="top:248px;">
    <h2 class="section__heading"><span class="section__marker"></span>Introduction</h2>
    <div class="section__body">
      <p>The technology industry is always evolving. Businesses and startups within the industry seek to innovate and take part in Research &amp; Development projects (R&amp;D) to stay ahead.<br>If your tech company works on innovative projects, you may be eligible for a tax offset under the R&amp;D Tax Incentive.</p>
    </div>
  </section>

  <div class="divider" style="left:47px; width:434px; top:390px;"></div>

  <section class="section" style="top:431px;">
    <h2 class="section__heading"><span class="section__marker"></span>Summary of R&amp;D Tax Incentive</h2>
    <div class="section__body">
      <p>The Australian government supports innovation by encouraging local businesses to develop new or improved products and original solutions. This support is offered through the Research &amp; Development (R&amp;D) Tax Incentive, reducing the financial risk involved in undertaking R&amp;D activities. By reducing the risks and costs associated with conducting R&amp;D, the incentive seeks to boost productivity, innovation and economic growth for the nation.</p>
      <p>The R&amp;D Tax Incentive offers a targeted tax offset of up to a 45% refund of costs for eligible Research &amp; Development activities that benefit Australia.</p>
      <p>Many businesses in Australia are already completing eligible R&amp;D activities without realising. In fact, only 30% of eligible small businesses conducting R&amp;D currently claim this tax incentive. You don’t need to be conducting experiments in a lab to qualify for R&amp;D incentives. If your business prides itself on innovation or is considering new developments, read on to find out more about how the R&amp;D Tax Incentive could provide cash back to your company.</p>
    </div>
  </section>

  <div class="footer-stripes"></div>
</article>

<article class="page page--inner">
  <div class="inner-band"></div>

  <section class="section section--intro-inner" style="top:68px;">
    <h2 class="section__heading"><span class="section__marker"></span>What is R&amp;D?</h2>
    <div class="section__body">
      <p>Research &amp; Development, or R&amp;D, involves conducting an experiment or trial to gain new knowledge. This new knowledge could be used to develop new or improved materials, products, devices, processes, software, or services. An experiment doesn’t have to be scientific, all it means it that at the start of this process you’re unaware of what the outcome will be and need to conduct further research, testing and trialling in order to overcome this uncertainty. The results seek to bridge the gap in knowledge that you started with.</p>
      <p class="lead">A wide range of businesses and industries conduct R&amp;D activities including (but not limited to):</p>
      <ul class="industry-list">
        <li>Professional services</li>
        <li>Manufacturing</li>
        <li>Agriculture</li>
        <li>Retail</li>
        <li>Fashion</li>
        <li>Science</li>
        <li>Technology</li>
      </ul>
    </div>
  </section>

  <div class="inner-lockup">
    <div class="wordmark"><span class="wordmark__square"></span>Veltmark</div>
    <span class="product">Quillbrook R&amp;D</span>
  </div>

  <div class="divider" style="left:47px; width:434px; top:377px;"></div>

  <section class="section" style="top:399px;">
    <h2 class="section__heading"><span class="section__marker"></span>Benefits of conducting R&amp;D activities</h2>
    <div class="section__body">
      <p>Research and Development helps to improve workforce skills and knowledge, venture capital opportunities, and technical proficiencies within a business. Innovation and cutting-edge solutions not only puts your company at the forefront of competition, it also supports the development of the Australian workforce and economy.</p>
      <p class="lead">Financial benefits of R&amp;D Tax Incentive</p>
      <p>Undertaking R&amp;D involves significant technical and financial risk. The R&amp;D Tax Incentive was introduced to encourage businesses in Australia to take on R&amp;D activities. Unlike a grant, you are not applying for funding or competing with other businesses for this financial incentive. Instead, the financial benefit is received in the way of tax offsets against expenses and is available to all eligible businesses.</p>
      <p>Small businesses (turnover below $20million) can receive a 45% R&amp;D tax offset against expenses in a financial year. Larger companies (over $20million aggregated turnover) can receive a 40% R&amp;D tax offset.</p>
      <p>Companies that have experienced a tax loss can also benefit from the R&amp;D Tax Incentive and could be eligible to offset 45cents for every dollar spent on R&amp;D activities.</p>
    </div>
  </section>

  <div class="footer-stripes"></div>
</article>

</body>
</html>
```